Emergency and Referral Vet Hospital promotional sticker design

We're looking at getting some stickers designed that we could give to clients to put on their cars for promotion and advertising. If they could also be suitable for a goodie bag for conference too that would be great. I like the look of water-colour backgrounds, we'll need to include our logo and probably our address (Unit 3/217 Marlowe Crescent Fairholt). We also have a hospital motto "... because they're family" if that could somehow be integrated, we only care for small animals (dogs, cats etc) but the design is very open to suggestion. Would love to see what you can create.

Industry/Entity Type

Veterinary

Colors
0054AA
0677BA
7BADD7
CADEEF
E8F1F8
0094D4
00A9DD
6FCCEA
C7EBF8
E9F6FB

Requirements
Nice to have
• Think beach vibes, blues maybe paw print shapes etc

```html
<!DOCTYPE html>
<html lang="en">
<head>
<meta charset="utf-8">
<title>Tidewell Vet Hospital – Because they're family</title>
<link rel="stylesheet" href="https://fonts.googleapis.com/css2?family=Cinzel:wght@500;600&family=Poppins:wght@400;500;600&display=swap">
<style>
  :root {
    --blue-deep: #0054AA;
    --blue-mid: #0677BA;
    --blue-bright: #0094D4;
    --blue-soft: #7BADD7;
    --blue-pale: #CADEEF;
    --paper: #e7e7ea;
    --paper-light: #f3f3f5;
    --white: #ffffff;
    --ink: #141414;
    --fur-light: #f0c79a;
    --fur-mid: #d9a36c;
    --fur-deep: #c08850;
  }
  * { margin: 0; padding: 0; box-sizing: border-box; }
  html, body { width: 1200px; height: 800px; overflow: hidden; background: var(--paper); }
  .sticker {
    position: relative;
    width: 1200px;
    height: 800px;
    overflow: hidden;
    background: linear-gradient(180deg, var(--paper) 0%, var(--paper-light) 100%);
  }
  .sticker__backdrop { position: absolute; inset: 0; }
  .motto {
    position: absolute;
    left: 63px;
    top: 62px;
    color: var(--white);
    font-family: "Cinzel", "Times New Roman", serif;
    font-weight: 600;
    font-size: 118px;
    line-height: 134px;
    letter-spacing: 1px;
    text-transform: lowercase;
  }
  .motto span { display: block; }
  .motto .motto__lead { text-transform: none; }
  .motto .motto__cap { text-transform: uppercase; }
  .photo {
    position: absolute;
  }
  .photo--kitten {
    left: 530px; top: 268px; width: 318px; height: 532px;
    border-radius: 150px 150px 0 0;
    background: radial-gradient(ellipse at 50% 30%, var(--fur-light) 0%, var(--fur-mid) 65%, var(--fur-deep) 100%);
  }
  .photo--dog {
    left: 855px; top: 338px; width: 345px; height: 462px;
    border-radius: 170px 120px 0 0;
    background: radial-gradient(ellipse at 45% 35%, var(--fur-light) 0%, var(--fur-mid) 60%, var(--fur-deep) 100%);
  }
  .contact {
    position: absolute;
    left: 0;
    top: 560px;
    width: 567px;
    color: var(--white);
    font-family: "Poppins", Arial, sans-serif;
  }
  .contact__row {
    display: flex;
    align-items: center;
    padding-left: 70px;
  }
  .contact__row--phone { height: 56px; }
  .contact__divider {
    height: 1px;
    margin: 15px 0 23px;
    background: rgba(255, 255, 255, 0.45);
  }
  .contact__icon { flex: none; width: 55px; height: 55px; margin-right: 12px; }
  .contact__phone { font-size: 28px; font-weight: 400; letter-spacing: 0.5px; }
  .contact__address { font-size: 26px; font-weight: 500; line-height: 33px; }
  .brand {
    position: absolute;
    left: 985px;
    top: 70px;
    width: 150px;
    display: flex;
    flex-direction: column;
    align-items: center;
    gap: 14px;
  }
  .brand__dot {
    width: 72px; height: 72px;
    border-radius: 50%;
    background: var(--blue-mid);
  }
  .brand__name {
    font-family: "Poppins", Arial, sans-serif;
    font-weight: 600;
    font-size: 30px;
    color: var(--ink);
    letter-spacing: 0.5px;
  }
</style>
</head>
<body>
<main class="sticker">
  <svg class="sticker__backdrop" width="1200" height="800" viewBox="0 0 1200 800" aria-hidden="true">
    <defs>
      <linearGradient id="blueWash" x1="0" y1="1" x2="1" y2="0">
        <stop offset="0" stop-color="#0054AA"/>
        <stop offset="0.45" stop-color="#0677BA"/>
        <stop offset="0.75" stop-color="#3f93cc"/>
        <stop offset="1" stop-color="#a9c9e8"/>
      </linearGradient>
    </defs>
    <polygon points="0,0 940,0 527,800 0,800" fill="url(#blueWash)"/>
  </svg>

  <div class="photo photo--dog" role="img" aria-label="Photo of a smiling golden retriever lying on a white fluffy rug"></div>
  <div class="photo photo--kitten" role="img" aria-label="Photo of a ginger kitten sitting upright"></div>

  <h1 class="motto">
    <span class="motto__lead">… <span class="motto__cap" style="display:inline">B</span>ecause</span>
    <span>they're</span>
    <span>family</span>
  </h1>

  <section class="contact">
    <div class="contact__row contact__row--phone">
      <svg class="contact__icon" viewBox="0 0 56 56" aria-hidden="true">
        <circle cx="28" cy="28" r="26" fill="none" stroke="#fff" stroke-width="2"/>
        <path d="M20 19c1-1 2.5-1 3.2 0l2.3 3.2c.6.9.4 2-.4 2.7l-1.4 1.1c1.2 2.6 3.2 4.6 5.8 5.8l1.1-1.4c.7-.8 1.8-1 2.7-.4l3.2 2.3c1 .7 1 2.2 0 3.2l-1.5 1.5c-1.2 1.2-3 1.5-4.5.8-5.2-2.4-9.3-6.5-11.7-11.7-.7-1.5-.4-3.3.8-4.5z" fill="#fff"/>
        <path d="M30 18a9 9 0 0 1 8 8M30 14a13 13 0 0 1 12 12" fill="none" stroke="#fff" stroke-width="2" stroke-linecap="round"/>
      </svg>
      <span class="contact__phone">(08) 9555 0142</span>
    </div>
    <div class="contact__divider"></div>
    <div class="contact__row">
      <svg class="contact__icon" viewBox="0 0 56 56" aria-hidden="true">
        <circle cx="28" cy="28" r="26" fill="none" stroke="#fff" stroke-width="2"/>
        <path d="M28 14a9 9 0 0 0-9 9c0 7 9 17 9 17s9-10 9-17a9 9 0 0 0-9-9z" fill="#fff"/>
        <circle cx="28" cy="23" r="3.3" fill="#0677BA"/>
      </svg>
      <address class="contact__address" style="font-style:normal">Unit 3/217 Marlowe<br>Crescent Fairholt, WA 6170</address>
    </div>
  </section>

  <div class="brand">
    <div class="brand__dot" aria-hidden="true"></div>
    <span class="brand__name">Tidewell</span>
  </div>
</main>
</body>
</html>
```